Window company.

Hello,

We are a small family business located in Madrid, Spain that works nationwide to fix, change or mount the windows of your home / premises.

The group of possible clients to whom the flyer is focused ranges from 30 to 65 years, families in general who want comfort at home and extra savings every year in heating.

It must include not only graphics and a striking aesthetic in accordance with the concepts of wanting to reach / transmit the final product to the customer to sell the product.

Details to also include:

-Brief history of the company and its foundation in 2006. It will be subsequently translated into Spanish so put in words what you consider necessary so that the client stays with the concept that we are professionals.

--Specialized in exterior aluminum and PVC carpentry.

-We move to your home for a first visit and we provide the budget totally free without any commitment.

- Also payment facilities; up to 3 times, without interest.

-Contact details of the company. (WhatsApp, email, phone and location)
Open: Mon - Friday 11,00am - 9pm
Saturday: 12,00am - 7pm
Sunday: Closed

Also as a suggestion, to decide on your own, graphics of types of window openings, if you consider that anything that is striking for the client so it wonr be yet another advertising flyer.

We are open to all kinds of ideas, all of them involving marketing branding.

We are open to any type of idea and we want to stand out, the construction world is tough and we have an idea to grow, taking into account that it must not only be beautiful but commercial to attract potential customers with all kinds of purchasing power.

Thank you.

```html
<!DOCTYPE html>
<html lang="en">
<head>
<meta charset="utf-8">
<title>Ventara – Windows Flyer</title>
<link href="https://fonts.googleapis.com/css2?family=Open+Sans:wght@400;600;700&family=Montserrat:wght@300;400&display=swap" rel="stylesheet">
<style>
  :root {
    --brand-red: #cc1f3f;
    --brand-red-dark: #9c0f2a;
    --flap-red: #8a0c22;
    --paper: #ffffff;
    --panel-grey: #e8e9ea;
    --text-dark: #2b2b2b;
    --text-muted: #9b9b9b;
    --logo-taupe: #a89f93;
  }
  * { margin: 0; padding: 0; box-sizing: border-box; }
  html, body { width: 848px; height: 1200px; overflow: hidden; background: var(--paper); }
  .flyer {
    position: relative;
    width: 848px;
    height: 1200px;
    overflow: hidden;
    background: var(--paper);
    font-family: "Open Sans", Arial, sans-serif;
  }
  .backdrop { position: absolute; inset: 0; }

  .brand {
    position: absolute;
    left: 50px; top: 78px;
    display: flex; align-items: center; gap: 12px;
  }
  .brand-square { width: 22px; height: 22px; background: var(--brand-red); }
  .brand-name {
    font-weight: 700; font-size: 30px; letter-spacing: 1px;
    color: var(--logo-taupe);
  }

  .quote-call {
    position: absolute; right: 46px; top: 28px; text-align: right;
    color: var(--brand-red);
  }
  .quote-call .lead { font-weight: 400; font-size: 28px; line-height: 32px; }
  .quote-call .phone { font-weight: 700; font-size: 28px; line-height: 32px; }

  .offer-panel {
    position: absolute; left: 61px; top: 574px; width: 358px; height: 527px;
    background: linear-gradient(180deg, var(--brand-red) 0%, var(--brand-red-dark) 100%);
    color: var(--paper);
  }
  .offer-title {
    position: absolute; left: 33px; top: 30px;
    font-size: 23px; font-weight: 400; letter-spacing: -0.3px;
  }
  .offer-title strong { font-weight: 700; }
  .offer-rule {
    position: absolute; left: 33px; top: 70px; width: 277px; height: 2px; background: var(--paper);
  }
  .offer-list { position: absolute; left: 46px; top: 100px; width: 300px; list-style: none; }
  .offer-list li {
    position: relative; font-weight: 700; font-size: 22px; line-height: 27px;
    letter-spacing: 0.2px; margin-bottom: 31px;
  }
  .offer-list li::before {
    content: "•"; position: absolute; left: -12px; top: 0; font-size: 14px;
  }

  .about {
    position: absolute; left: 463px; top: 692px; width: 340px;
  }
  .about-title {
    display: flex; align-items: center; gap: 24px;
    font-size: 23px; font-weight: 400; color: var(--text-dark); letter-spacing: -0.3px;
  }
  .about-title strong { font-weight: 700; }
  .about-title .rule { flex: 1; height: 2px; background: var(--text-dark); }
  .about-text {
    margin-top: 14px; font-family: "Montserrat", Arial, sans-serif; font-weight: 400;
    font-size: 15px; line-height: 19.5px; letter-spacing: 0.5px; color: var(--text-muted);
  }
  .about-text + .about-text { margin-top: 19px; }

  .hours {
    position: absolute; left: 463px; top: 932px;
    display: grid; grid-template-columns: 62px auto; row-gap: 0;
    font-size: 19.5px; line-height: 30.5px; font-weight: 700;
  }
  .hours dt { color: #111; font-weight: 400; }
  .hours dd { color: var(--brand-red); grid-column: 2; }

  .footer-address {
    position: absolute; left: 96px; top: 1125px; width: 330px;
    display: flex; align-items: center; gap: 20px; color: var(--paper);
  }
  .footer-address p {
    flex: 1; text-align: center; font-size: 15.5px; line-height: 23px; font-weight: 400;
  }
  .footer-phone {
    position: absolute; left: 529px; top: 1128px;
    display: flex; align-items: center; gap: 17px; color: var(--paper);
    font-weight: 700; font-size: 27px;
  }
</style>
</head>
<body>
<div class="flyer">
  <svg class="backdrop" width="848" height="1200" viewBox="0 0 848 1200">
    <defs>
      <linearGradient id="photoTone" x1="0" y1="0" x2="1" y2="1">
        <stop offset="0" stop-color="#b9c99a"/>
        <stop offset="0.35" stop-color="#a3765a"/>
        <stop offset="0.7" stop-color="#6d5246"/>
        <stop offset="1" stop-color="#2f3a52"/>
      </linearGradient>
      <linearGradient id="silver" x1="0" y1="0" x2="1" y2="0">
        <stop offset="0" stop-color="#6f6f6f"/>
        <stop offset="0.5" stop-color="#f2f2f2"/>
        <stop offset="1" stop-color="#7a7a7a"/>
      </linearGradient>
      <linearGradient id="footerRed" x1="0" y1="0" x2="1" y2="0">
        <stop offset="0" stop-color="#cc1f3f"/>
        <stop offset="1" stop-color="#a8112d"/>
      </linearGradient>
    </defs>

    <!-- grey content panel -->
    <rect x="0" y="600" width="848" height="600" fill="var(--panel-grey)"/>

    <!-- photo zone -->
    <path role="img" aria-label="Photo: a worker in a yellow hard hat and safety glasses fitting a window pane with suction lifters"
          d="M0 300 Q330 120 848 140 L848 660 Q640 590 420 600 L0 650 Z" fill="url(#photoTone)"/>

    <!-- top swoosh bands -->
    <path d="M0 292 Q330 110 848 118 L848 140 Q330 128 0 300 Z" fill="url(#silver)"/>
    <path d="M0 312 Q330 135 848 150 L848 140 Q330 122 0 300 Z" fill="var(--brand-red)"/>

    <!-- lower swoosh bands -->
    <path d="M0 645 Q200 600 420 598 Q640 590 848 656 L848 672 Q640 608 420 612 Q200 615 0 662 Z" fill="var(--brand-red)"/>
    <path d="M0 662 Q200 615 420 612 Q640 608 848 672 L848 694 Q640 628 420 628 Q200 632 0 680 Z" fill="url(#silver)"/>

    <!-- panel flap -->
    <path d="M47 627 L61 574 L61 627 Z" fill="var(--flap-red)"/>

    <!-- footer band -->
    <path d="M0 1106 Q420 1090 848 1010 L848 1200 L0 1200 Z" fill="var(--paper)"/>
    <path d="M0 1112 Q420 1098 848 1022 L848 1200 L0 1200 Z" fill="url(#footerRed)"/>
  </svg>

  <div class="brand">
    <span class="brand-square"></span>
    <span class="brand-name">VENTARA</span>
  </div>

  <div class="quote-call">
    <p class="lead">Call us for free quote</p>
    <p class="phone">+34 600 41 72 95</p>
  </div>

  <section class="offer-panel">
    <h2 class="offer-title">WHAT <strong>WE OFFER?</strong></h2>
    <div class="offer-rule"></div>
    <ul class="offer-list">
      <li>Specialized in exterior aluminum and PVC carpentry.</li>
      <li>We move to your home for a first visit and we provide the budget totally free without any commitment.</li>
      <li>Also payment facilities; up to 3 times, without interest.</li>
    </ul>
  </section>

  <section class="about">
    <h2 class="about-title"><span>WHO <strong>WE ARE?</strong></span><span class="rule"></span></h2>
    <p class="about-text">We are a small family business located in Madrid, Spain that works nationwide to fix, change or mount the windows of your home / premises. We are founded in 2006.</p>
    <p class="about-text">We offer full service from initial contact to final fitting, making sure all projects are finsied to the highest standard.</p>
  </section>

  <dl class="hours">
    <dt>Open:</dt>
    <dd>Mon - Friday 11,00am - 9pm</dd>
    <dd>Saturday: 12,00am - 7pm</dd>
    <dd>Sunday: Closed</dd>
  </dl>

  <div class="footer-address">
    <svg width="30" height="46" viewBox="0 0 30 46" aria-hidden="true">
      <path d="M15 0 C6.7 0 0 6.7 0 15 C0 26 15 46 15 46 C15 46 30 26 30 15 C30 6.7 23.3 0 15 0 Z" fill="#111"/>
      <circle cx="15" cy="15" r="5.5" fill="var(--brand-red)"/>
    </svg>
    <p>Pol. Ind. Valdeolmos III, Nave 14<br>Alcobendas, Spain 28100</p>
  </div>

  <div class="footer-phone">
    <svg width="38" height="36" viewBox="0 0 38 36" aria-hidden="true">
      <path d="M7 3 L13 3 L16 11 L12 14 Q15 21 22 24 L25 20 L33 23 L33 29 Q33 33 28 33 Q6 31 4 8 Q4 3 7 3 Z" fill="#111"/>
      <path d="M21 4 Q31 6 33 15" stroke="#111" stroke-width="2.5" fill="none"/>
      <path d="M21 9 Q27 10 28 16" stroke="#111" stroke-width="2.5" fill="none"/>
    </svg>
    <span>+34 600 41 72 95</span>
  </div>
</div>
</body>
</html>
```